Create 8 Featured Images for 8 Blog articles

We're looking for a an individual with a background in graphic design to creatively process images for a popular product blog. This project will be to create 8 Featured images for our Blog which can be seen here http://www.brakwelsupply.com/blog the featured image is the large image which can be seen through the link above. If all goes well with this first project then there will be many additional graphic design projects available for our blog.

1. My Pool Pump is Running Too Hot - Article can be seen here http://www.brakwelsupply.com/blog/why-is-my-motor-running-hot/ We would like an Image of 750 x 250 of a pool pump in the desert or under the sun. Something obvious. We are trying to convey the message of an extremely hot pump. For the Desert or Sun use an image of your liking and for the pool pump use the attached image labeled “Hot Pump.jpg” (remove text from this image) Add text to image which says "Pool Pump Running Hot?"

2. Leaking pool pump - Article can be seen here http://www.brakwelsupply.com/blog/leaking-pool-pump/ Image to be created would be a leaking pool pump which is gushing out water similar to what is shown here http://www.tandrick-aqua-care.com/pool-closings.html but we would like for this to look much cleaner. The background of the image should be similar in color and style of the image backgrounds which can be seen here http://www.brakwelsupply.com/blog/ For the pool pump use the attached image labeled “Leaking Pump.jpg” and then photoshop gushing water out of the pump. Add text to image which says "Leaking Pool Pump?"

3. Can I go with a higher Horse Power Pump - article can be seen here http://www.brakwelsupply.com/blog/can-go-higher-horsepower-pump/ Image of a large pool pump vs. a small pump - You can exagerate the size of the large pump and exagerate the size of the small pump. The idea is to show a really big looking pump vs. a small looking pump. Attached image for the large pump is labeled “Large Pump.jpg” and Attached image of small pump is labeled “Small Pump.jpg” Add text to image which says "Large HP Vs. Small HP"

4. Pool Pump Trips Breaker - Article can be seen here http://www.brakwelsupply.com/blog/pool-pump-trips-breaker-gfci/ This will be a simple Image of a pool pump and a breaker spaced out evenly. Use attached image of of pool pump labeled “Pool Pump Breaker.jpg” and for the breaker use the attached image labeled “Breaker.jpg” Add text to image which says "Pool Pump Tripping Breaker?"

5. Why is my spa dirty? - Article can be seen here http://www.brakwelsupply.com/blog/spa-dirty/ use attached image labeled spa set on white backgroud with Text which says "Dirty Spa?"

6. Think You’re Cut out to Replace Your Pool Pump Motor? Take This Quiz - Article here -
http://www.brakwelsupply.com/blog/think-youre-cut-replace-pool-pump-motor-take-quiz/ Image integrating Quiz.jpg image and motor.jpg image with Text labeled "Take the Pool Motor Replacement Quiz"

7. Can I repair my pool Equipment - article here http://www.brakwelsupply.com/blog/can-i-repair-my-pool-equipment/ - A guy holding tools with a question mark thought bubble.

8. How Long should I run my pool pump article here -http://www.brakwelsupply.com/blog/how-long-should-i-run-my-pool-pump/ - image of a pool pump along with a man looking at his watch.

```html
<!DOCTYPE html>
<html lang="en">
<head>
<meta charset="utf-8">
<title>Brakwel Supply Blog</title>
<link rel="stylesheet" href="https://fonts.googleapis.com/css2?family=Open+Sans:wght@400;600;700&family=Bebas+Neue&family=Arimo:wght@700&display=swap">
<style>
  :root {
    --header-blue: #1e6597;
    --page-bg: #f2f2f2;
    --card-bg: #ffffff;
    --border: #dcdcdc;
    --accent: #e2622b;
    --button-blue: #3a89b7;
    --button-border: #2a6e97;
    --text: #555555;
    --muted: #a4a4a4;
    --heading: #555555;
    --sky-top: #6fb3e6;
    --sky-mid: #b4daf4;
    --sky-low: #e9f5fd;
    --breaker-dark: #2c2c2e;
    --breaker-light: #8c8f93;
    --pump-dark: #1d1d1f;
    --pump-mid: #3a3b3e;
  }
  * { box-sizing: border-box; margin: 0; padding: 0; }
  html, body { width: 1200px; height: 706px; overflow: hidden; }
  body {
    position: relative;
    background: var(--page-bg);
    font-family: "Open Sans", Arial, sans-serif;
    color: var(--text);
  }
  .site-header {
    position: absolute; left: 0; top: 0; width: 1200px; height: 76px;
    background: var(--header-blue);
  }
  .brand {
    position: absolute; left: 30px; top: 22px;
    display: flex; align-items: center; gap: 10px;
    color: #ffffff; font-weight: 700; font-size: 25px; letter-spacing: 0.5px;
  }
  .brand-dot { width: 26px; height: 26px; border-radius: 50%; background: #ffffff; }
  .main-nav {
    position: absolute; right: 60px; top: 29px;
    display: flex; gap: 34px;
  }
  .main-nav a { color: #ffffff; text-decoration: none; font-size: 14px; letter-spacing: 0.2px; }

  .post-card {
    position: absolute; left: 28px; top: 121px; width: 751px; height: 600px;
    background: var(--card-bg); border: 1px solid var(--border);
  }
  .featured {
    position: absolute; left: 4px; top: 3px; width: 742px; height: 242px;
    background:
      radial-gradient(ellipse 180px 70px at 80px 150px, rgba(255,255,255,0.75), transparent),
      radial-gradient(ellipse 200px 80px at 680px 180px, rgba(255,255,255,0.8), transparent),
      radial-gradient(ellipse 260px 60px at 370px 230px, rgba(255,255,255,0.7), transparent),
      linear-gradient(180deg, var(--sky-top) 0%, var(--sky-mid) 55%, var(--sky-low) 100%);
    overflow: hidden;
  }
  .featured-title {
    position: absolute; left: 0; right: 0; top: 4px;
    text-align: center; font-family: "Bebas Neue", "Oswald", sans-serif;
    font-size: 53px; color: #ffffff; letter-spacing: 0.5px;
    text-shadow: 0 2px 0 #b8c3cc, 0 3px 6px rgba(0,0,0,0.35);
  }
  .breaker-photo {
    position: absolute; left: 172px; top: 70px; width: 113px; height: 158px;
    background: linear-gradient(90deg, var(--breaker-light) 0%, var(--breaker-dark) 25%, var(--breaker-dark) 75%, var(--breaker-light) 100%);
    border-radius: 3px;
  }
  .pump-photo {
    position: absolute; left: 362px; top: 75px; width: 253px; height: 145px;
    background: linear-gradient(180deg, var(--pump-mid) 0%, var(--pump-dark) 100%);
    border-radius: 40px 12px 8px 8px;
  }
  .post-title {
    position: absolute; left: 50px; top: 293px;
    font-family: "Arimo", Arial, sans-serif; font-weight: 700;
    font-size: 27px; color: var(--accent);
  }
  .post-meta {
    position: absolute; left: 50px; top: 357px;
    display: flex; align-items: center; font-size: 13px; color: var(--text);
  }
  .post-meta .item { display: flex; align-items: center; gap: 6px; margin-right: 13px; }
  .post-meta svg { display: block; }
  .post-excerpt {
    position: absolute; left: 50px; top: 408px; width: 662px;
    font-size: 14px; line-height: 23px; color: var(--text);
  }
  .read-more {
    position: absolute; left: 603px; top: 520px; width: 96px; height: 41px;
    background: var(--button-blue); border: 1px solid var(--button-border); border-radius: 3px;
    color: #ffffff; font-size: 12px; display: flex; align-items: center; justify-content: center;
  }

  .sidebar {
    position: absolute; left: 808px; top: 121px; width: 360px; height: 600px;
    background: var(--card-bg); border: 1px solid var(--border); border-radius: 3px;
  }
  .search { position: absolute; left: 30px; top: 30px; display: flex; }
  .search-field {
    width: 259px; height: 34px; border: 1px solid #cccccc; border-right: none;
    font-size: 14px; color: #777777; padding: 7px 4px;
  }
  .search-button {
    width: 40px; height: 34px; background: var(--button-blue); border: 1px solid var(--button-border);
    display: flex; align-items: center; justify-content: center;
  }
  .widget-title {
    position: absolute; left: 30px;
    font-family: "Arimo", Arial, sans-serif; font-weight: 700; font-size: 13px;
    color: var(--heading); letter-spacing: 0.3px;
  }
  .recent-title { top: 113px; }
  .archive-title { top: 488px; }
  .recent-list { position: absolute; left: 30px; top: 144px; width: 297px; list-style: none; }
  .recent-list li {
    border-bottom: 1px solid #e6e6e6; padding: 9px 0; font-size: 14px; line-height: 18px;
    height: 57px;
  }
  .recent-list .link { color: var(--muted); }
  .recent-list .date { color: var(--accent); }
  .archive-list { position: absolute; left: 30px; top: 518px; width: 297px; list-style: none; }
  .archive-list li {
    display: flex; align-items: center; gap: 8px; font-size: 14px; color: var(--muted);
    border-bottom: 1px solid #e6e6e6; height: 38px;
  }
</style>
</head>
<body>
  <header class="site-header">
    <div class="brand"><span class="brand-dot"></span>BRAKWELSUPPLY.COM</div>
    <nav class="main-nav">
      <a href="#">SHOP BRAKWELSUPPLY</a>
      <a href="#">MY ACCOUNT</a>
      <a href="#">VIEW CART</a>
    </nav>
  </header>

  <article class="post-card">
    <div class="featured" role="img" aria-label="Bright sky with white clouds">
      <div class="featured-title">POOL PUMP TRIPPING BREAKER?</div>
      <div class="breaker-photo" role="img" aria-label="Double-pole GFCI circuit breaker"></div>
      <div class="pump-photo" role="img" aria-label="Black pool pump with motor"></div>
    </div>
    <h2 class="post-title">Getting DE Powder Back in Your Pool</h2>
    <div class="post-meta">
      <span class="item">
        <svg width="13" height="13" viewBox="0 0 13 13"><rect x="0.5" y="1.5" width="12" height="11" fill="none" stroke="#e2622b"/><rect x="0.5" y="1.5" width="12" height="3" fill="#e2622b"/><path d="M3 7h2M6 7h2M9 7h2M3 10h2M6 10h2M9 10h2" stroke="#e2622b"/></svg>
        December 17, 2014
      </span>
      <span class="item">
        <svg width="11" height="13" viewBox="0 0 11 13"><circle cx="5.5" cy="3.5" r="3" fill="#e2622b"/><path d="M0 13c0-4 2.5-5.5 5.5-5.5S11 9 11 13z" fill="#e2622b"/></svg>
        Dana Whitmore
      </span>
      <span class="item">
        <svg width="14" height="12" viewBox="0 0 14 12"><path d="M7 1C3.5 1 1 3 1 5.3c0 1.3.8 2.4 2 3.1L2.5 11l3-2c.5.1 1 .1 1.5.1 3.5 0 6-2 6-4.4S10.5 1 7 1z" fill="none" stroke="#e2622b"/></svg>
        2 Comments
      </span>
    </div>
    <p class="post-excerpt">Few things are more frustrating than to see the very stuff that is supposed to be filtering your pool water leaking into the pool.&nbsp; The common culprit involved in DE powder going back into your pool is torn grids but there are a number of other causes as well.&nbsp; Here are a few things to check to help you troubleshoot this annoying problem.</p>
    <a class="read-more">READ MORE</a>
  </article>

  <aside class="sidebar">
    <div class="search">
      <div class="search-field">Search...</div>
      <div class="search-button">
        <svg width="14" height="14" viewBox="0 0 14 14"><circle cx="6" cy="6" r="4.5" fill="none" stroke="#fff" stroke-width="2"/><path d="M9.3 9.3l3.5 3.5" stroke="#fff" stroke-width="2.4" stroke-linecap="round"/></svg>
      </div>
    </div>
    <h3 class="widget-title recent-title">OUR RECENT POSTS &amp; ARTICLES</h3>
    <ul class="recent-list">
      <li><span class="link">Getting DE Powder Back in Your Pool</span><br><span class="date">December 17, 2014</span></li>
      <li><span class="link">Are Generic Parts Better Than OEM?</span><br><span class="date">December 12, 2014</span></li>
      <li><span class="link">5 Biggest Problems with Pool Filters</span><br><span class="date">December 12, 2014</span></li>
      <li><span class="link">Pool Pump Trips Breaker / GFCI</span> <span class="date">October 29, 2014</span></li>
      <li><span class="link">Can I Go With A Higher Horsepower Pump?</span><br><span class="date">October 23, 2014</span></li>
    </ul>
    <h3 class="widget-title archive-title">ARCHIVES</h3>
    <ul class="archive-list">
      <li><svg width="13" height="13" viewBox="0 0 13 13"><rect x="0.5" y="1.5" width="12" height="11" fill="none" stroke="#e2622b"/><rect x="0.5" y="1.5" width="12" height="3" fill="#e2622b"/><path d="M3 7h2M6 7h2M9 7h2M3 10h2M6 10h2M9 10h2" stroke="#e2622b"/></svg>December 2014</li>
      <li><svg width="13" height="13" viewBox="0 0 13 13"><rect x="0.5" y="1.5" width="12" height="11" fill="none" stroke="#e2622b"/><rect x="0.5" y="1.5" width="12" height="3" fill="#e2622b"/><path d="M3 7h2M6 7h2M9 7h2M3 10h2M6 10h2M9 10h2" stroke="#e2622b"/></svg>October 2014</li>
    </ul>
  </aside>
</body>
</html>
```